Harbor Dental, LLC business card project

Business card to be designed with current logo.
Dental office- please keep design of card that looks clean and professional.
Please include the following info:
Harbor Dental, LLC
Dr. Corinne Pelham
3187 Elmwood
Alderbrook, PA 19347
610-392-7158
harbordental.office@quillmail.net
Updates
Hello everyone-
Project Deadline Extended
Reason: Just got back from overseas- will look at all designs and provide feedback. Thank you!
Project Deadline Extended
Reason: Polling my friends for the final selection-
thank you to all those that participated- so many talented designers!
Business

```html
<!DOCTYPE html>
<html lang="en">
<head>
<meta charset="utf-8">
<title>Harbor Dental, LLC – Business Card</title>
<link rel="stylesheet" href="https://fonts.googleapis.com/css2?family=Saira:wght@400;500&family=Arimo:wght@400;700&display=swap">
<style>
  :root {
    --bg: #d9d9d9;
    --card: #ffffff;
    --green-light: #9cc31f;
    --green-dark: #5e9a2c;
    --rule: #c9dc96;
    --shadow: rgba(0, 0, 0, 0.18);
  }
  * { box-sizing: border-box; margin: 0; padding: 0; }
  html, body {
    width: 1200px;
    height: 901px;
    overflow: hidden;
    background: var(--bg);
  }
  .sheet {
    width: 1200px;
    height: 901px;
    display: flex;
    flex-direction: column;
    align-items: center;
    justify-content: center;
    gap: 40px;
  }
  .card {
    position: relative;
    width: 620px;
    height: 354px;
    background: var(--card);
    box-shadow: 0 6px 18px var(--shadow);
  }
  .brand {
    display: flex;
    align-items: center;
    gap: 12px;
    font-family: "Saira", sans-serif;
    font-weight: 400;
    color: var(--green-dark);
    white-space: nowrap;
  }
  .brand-dot {
    border-radius: 50%;
    background: var(--green-light);
    flex: none;
  }
  /* front */
  .card-front .brand {
    position: absolute;
    left: 50%;
    top: 50%;
    transform: translate(-50%, -50%);
    font-size: 40px;
  }
  .card-front .brand-dot { width: 22px; height: 22px; }
  /* back */
  .card-back .brand {
    position: absolute;
    left: 48px;
    top: 40px;
    font-size: 32px;
  }
  .card-back .brand-dot { width: 18px; height: 18px; }
  .holder {
    position: absolute;
    left: 54px;
    top: 132px;
    width: 340px;
    font-family: "Saira", sans-serif;
    font-weight: 500;
    font-size: 21px;
    color: var(--green-light);
    padding-bottom: 6px;
    border-bottom: 1px solid var(--rule);
  }
  .address {
    position: absolute;
    left: 54px;
    top: 186px;
    font-family: "Arimo", sans-serif;
    font-size: 14px;
    line-height: 1.3;
    color: var(--green-dark);
    font-style: normal;
  }
  .address .company { font-weight: 700; }
  .contact {
    position: absolute;
    left: 50px;
    top: 268px;
    display: flex;
    gap: 22px;
    font-family: "Arimo", sans-serif;
    font-size: 14px;
    color: var(--green-dark);
  }
  .contact-item { display: flex; align-items: center; gap: 7px; }
  .contact-item svg { width: 12px; height: 12px; fill: var(--green-dark); }
</style>
</head>
<body>
<main class="sheet">
  <section class="card card-front" aria-label="Card front">
    <div class="brand"><span class="brand-dot"></span>Harbor Dental, LLC</div>
  </section>

  <section class="card card-back" aria-label="Card back">
    <div class="brand"><span class="brand-dot"></span>Harbor Dental, LLC</div>
    <h1 class="holder">Dr. Corinne Pelham</h1>
    <address class="address">
      <div class="company">Harbor Dental, LLC</div>
      <div>3187 Elmwood</div>
      <div>Alderbrook, PA 19347</div>
    </address>
    <div class="contact">
      <span class="contact-item">
        <svg viewBox="0 0 12 12" aria-hidden="true"><path d="M2.4 0.6 4.2 2.8 3.3 4.1c.6 1.5 1.6 2.6 3.1 3.3l1.3-.9 2.2 1.8-1 2.1C5.1 10.4 1.3 6.6.6 1.5z"/></svg>
        610-392-7158
      </span>
      <span class="contact-item">
        <svg viewBox="0 0 12 12" aria-hidden="true"><path d="M0 2h12v8H0z M1 3v.4l5 3.2 5-3.2V3z" fill-rule="evenodd"/></svg>
        harbordental.office@quillmail.net
      </span>
    </div>
  </section>
</main>
</body>
</html>
```